TK Motorwerk braucht Werbeflyer
Zielgruppe
An Fahrzeugen:
-Leistungsteigerung
-Codier- und Nachrüstungen an ZRD und HOL Fahrzeugen
- KFZ Servicearbeiten Schwerpunkt ZRD
-Reifenhandel und Montage
- Autohandel
- Autoglaserbetrieb mit Zertifizierung und Versicherungsabwicklung
Aufgabenstellung
Größe soll DIN A5 sein.
Flyerdesign soll für die Vorder- und Rückseite erstellt werden.
Design bitte ähnlich wie Visitenkarte was ich hochgeladen habe
Die Vorderseite soll sich konzentieren auf:
Leistungsteigerung:
Es gibt bei uns zwei Alternativen
Softwareoptimierung und Tuningboxen
Softwareootimierung ab 299€
Tuningboxen ab 499€
Weitere Leistungen für die vorderseite :
Gaspedaltuning für direktere Gasannahme ab 149€
DPF abschaltung und Vmax aufhebung ab 199€
Rückseite soll sich auf den Rest konzentieren diese Wären:
- Codierarbeiten und Nachrüstarbeiten an ZRD und HOL Fahrzeugen
- Fehlerdiagnose, Steuergeräte einlernen und Softwareupdates an ZRD Fahrzeugen
- KFZ Servicearbeiten (Schwerpunkt ZRD)
- Reifenhandel und Montage
- Autoglas
- Autohandel Kauf und Verkauf im Kundenauftrag
An der Rückseite sollten kurze Texte geschrieben werden für die Leistungen
Für vorderseite bitte zwei Ausführungen einmal wie hier beschrieben und einmal mit dem Zusatz:
Nur bis zum 15. Dezember 10% Rabatt auf Softwareoptimierung und Tuningboxen bei Vorlage des Flyers

```html
<!DOCTYPE html>
<html lang="de">
<head>
<meta charset="utf-8">
<title>TK Motorwerk – Flyer Vorderseite</title>
<link rel="stylesheet" href="https://fonts.googleapis.com/css2?family=Oswald:wght@400;500;600;700&display=swap">
<style>
  :root {
    --page-bg: #ffffff;
    --flyer-navy: #0b1624;
    --flyer-deep: #050b14;
    --band-red: #b30d16;
    --band-red-dark: #6e060c;
    --text-white: #ffffff;
    --text-ice: #dde7f2;
    --badge-grey: #c9ced6;
  }
  * { margin: 0; padding: 0; box-sizing: border-box; }
  html, body {
    width: 1200px; height: 1200px; overflow: hidden;
    background: var(--page-bg);
    font-family: "Oswald", "Arial Narrow", sans-serif;
  }
  .flyer {
    position: absolute; left: 60px; top: 210px;
    width: 1080px; height: 780px; overflow: hidden;
    background: radial-gradient(ellipse at 70% 60%, #13243a 0%, var(--flyer-navy) 55%, var(--flyer-deep) 100%);
  }
  .headlight-visual {
    position: absolute; left: 0; top: 205px; width: 560px; height: 575px;
    background:
      radial-gradient(ellipse 40% 55% at 35% 45%, rgba(120,170,230,.55) 0%, rgba(40,80,140,.35) 45%, transparent 75%),
      linear-gradient(110deg, #0a1626 0%, #12294a 45%, rgba(11,22,36,0) 100%);
  }
  .title-band {
    position: absolute; left: 0; top: 55px; width: 100%; height: 150px;
    background: linear-gradient(90deg, var(--band-red) 0%, var(--band-red) 70%, var(--band-red-dark) 100%);
  }
  .headline {
    position: absolute; left: 270px; right: 40px; top: 26px;
    text-align: center; color: var(--text-white); text-transform: uppercase;
  }
  .headline-main {
    font-weight: 600; font-size: 64px; line-height: 1; letter-spacing: 11px;
  }
  .headline-sub {
    margin-top: 14px; font-weight: 600; font-size: 22px; line-height: 1; letter-spacing: 4px;
  }
  .brand-badge {
    position: absolute; left: 55px; top: 40px;
    width: 185px; height: 185px; border-radius: 50%;
    background: var(--badge-grey);
    display: flex; align-items: center; justify-content: center;
  }
  .brand-name {
    font-weight: 600; font-size: 26px; line-height: 1.1;
    color: var(--flyer-navy); text-align: center; letter-spacing: 1px;
  }
  .price-list {
    position: absolute; right: 60px; top: 0; width: 760px; height: 100%;
    list-style: none; color: var(--text-ice);
  }
  .price-item {
    position: absolute; right: 0;
    display: flex; justify-content: flex-end; align-items: center;
    transform: translateY(-50%); white-space: nowrap;
  }
  .price-item--software { top: 312px; }
  .price-item--boxes { top: 400px; }
  .price-item--pedal { top: 520px; }
  .price-item--dpf { top: 640px; }
  .service {
    font-weight: 500; font-size: 31px; line-height: 1.08; text-align: right;
  }
  .from {
    font-weight: 500; font-size: 30px; margin: 0 12px 0 20px;
  }
  .price {
    font-weight: 600; font-size: 70px; line-height: 1;
    min-width: 150px; text-align: right; white-space: nowrap;
  }
</style>
</head>
<body>
  <article class="flyer">
    <div class="headlight-visual" role="img" aria-label="Nahaufnahme eines leuchtenden LED-Scheinwerfers in Blautönen"></div>

    <header class="title-band">
      <div class="headline">
        <h1 class="headline-main">Volle Leistung durch</h1>
        <p class="headline-sub">Tuningboxen und Softwareoptimierung</p>
      </div>
    </header>

    <div class="brand-badge"><span class="brand-name">TK<br>Motorwerk</span></div>

    <ul class="price-list">
      <li class="price-item price-item--software"><span class="service">Softwareoptimierung</span><span class="from">ab</span><span class="price">299 €</span></li>
      <li class="price-item price-item--boxes"><span class="service">Tuningboxen</span><span class="from">ab</span><span class="price">499 €</span></li>
      <li class="price-item price-item--pedal"><span class="service">Gaspedaltuning<br>für direktere Gasannahme</span><span class="from">ab</span><span class="price">149 €</span></li>
      <li class="price-item price-item--dpf"><span class="service">DPF-Abschaltung<br>und Vmax-Aufhebung</span><span class="from">ab</span><span class="price">199 €</span></li>
    </ul>
  </article>
</body>
</html>
```